Vehicle Rental Hire in the Algarve - Portugal

We are opening a Vehicle Rental company in the Algarve - Portugal - this will attract both locals and Tourists visiting. So we want this website to capture the beautiful location we will be set in, along with the familiarity of a vehicle rental company. And to keep a colour scheme in Line with out Logo. We are Marlenic Vehicle Rental.

Industry/Entity Type

Vehicle Rental

Number of Pages Required

1 page

Requirements
Must have
• must be professional, and simple to use navigation bar - must also have a "make a reservation" box - similar to the screenshot attached - Under our logo it must read "Vehicle Rental"
Nice to have
• It needs to be in a colour scheme that fits in with our logo

```html
<!DOCTYPE html>
<html lang="en">
<head>
<meta charset="utf-8">
<title>Marlenic Vehicle Rental – Algarve</title>
<link href="https://fonts.googleapis.com/css2?family=Playfair+Display:wght@500;600;700&family=Roboto:wght@400;500&family=Mrs+Saint+Delafield&display=swap" rel="stylesheet">
<style>
:root{
  --blue:#1a17d6;
  --red:#c7302b;
  --red-soft:#dd8a86;
  --ink:#333;
  --muted:#555;
  --field:#f8eceb;
  --footer:#1c0404;
  --bar:#c52f29;
  --white:#fff;
}
*{box-sizing:border-box;margin:0;padding:0}
html,body{width:1200px;height:2993px;overflow:hidden}
body{position:relative;font-family:'Roboto',sans-serif;color:var(--ink);background:var(--white)}
.abs{position:absolute}
.serif{font-family:'Playfair Display',serif}

/* hero */
.hero{left:0;top:0;width:1200px;height:681px;
  background:linear-gradient(180deg,#cfd6dc 0%,#e6e2dc 40%,#d9d0c2 65%,#8c9474 85%,#6b6650 100%)}
.hero-car{right:0;top:60px;width:300px;height:621px;
  background:linear-gradient(160deg,#c9ccd1,#9da2a8 60%,#6b6e72)}
.header{left:112px;top:0;width:976px;height:92px;background:rgba(255,255,255,.9);border-radius:0 0 6px 6px}
.brand{left:18px;top:10px;display:flex;align-items:center;gap:8px}
.brand-mark{width:70px;height:70px;border:2px solid var(--blue);border-radius:50%;display:flex;flex-direction:column;align-items:center;justify-content:center}
.brand-name{font-size:17px;font-weight:500;color:var(--blue);line-height:1}
.brand-sub{font-size:8px;color:var(--blue);margin-top:3px}
.nav{right:18px;top:25px;display:flex;align-items:center;gap:40px;font-size:16px;font-weight:500;color:#444}
.nav span{display:flex;align-items:center;gap:5px}
.lang{border:1px solid var(--red);border-radius:3px;padding:10px 12px;font-weight:400;color:#333}
.flag{width:26px;height:16px;background:linear-gradient(180deg,#b22 0 14%,#fff 14% 28%,#b22 28% 42%,#fff 42% 57%,#b22 57% 71%,#fff 71% 85%,#b22 85%);position:relative}
.flag::before{content:"";position:absolute;left:0;top:0;width:11px;height:9px;background:#2a3a8c}
.hero-title{left:109px;top:192px;font-size:33px;font-weight:600;color:var(--blue)}
.hero-script{left:106px;top:222px;font-family:'Mrs Saint Delafield',cursive;font-size:92px;color:var(--red);white-space:nowrap}

/* reservation */
.booking{left:109px;top:373px;width:982px;height:280px;background:var(--white);border:4px solid #eee;border-radius:6px}
.booking h2{position:absolute;left:16px;top:18px;font-size:26px;font-weight:500;color:var(--blue)}
.booking .rule{position:absolute;left:16px;right:16px;top:56px;height:1px;background:#e6b3b0}
.field{position:absolute;height:40px;background:var(--field);border-radius:3px;font-size:15px;color:#444;display:flex;align-items:center;padding:0 14px;justify-content:space-between}
.label{position:absolute;font-size:14px;color:#444}
.chk{position:absolute;left:33px;top:123px;font-size:12px;color:#444;display:flex;align-items:center;gap:8px}
.chk i{width:11px;height:11px;border:1px solid #333;display:block}
.search{position:absolute;left:789px;top:212px;width:172px;height:40px;background:var(--blue);color:#fff;font-size:16px;font-weight:500;display:flex;align-items:center;justify-content:center;border-radius:2px}

/* why */
.center{left:0;width:1200px;text-align:center}
.sec-title{font-size:33px;font-weight:600;color:var(--blue)}
.divider{width:36px;height:1px;background:var(--red);margin:0 auto}
.lead{font-size:16px;line-height:28px;color:#333}
.feature{width:300px;text-align:center}
.feature .ring{width:118px;height:118px;border:2px solid var(--red);border-radius:50%;margin:0 auto;display:flex;align-items:center;justify-content:center}
.feature h3{font-family:'Playfair Display',serif;font-size:23px;font-weight:600;color:var(--red);margin-top:16px}
.feature p{font-size:14px;line-height:22px;color:#444;margin-top:6px}

/* testimonial */
.testi-bg{left:0;top:1271px;width:1200px;height:569px;
  background:linear-gradient(180deg,#4d7fae 0%,#7fa6c4 25%,#5b6b58 55%,#3f4a2c 80%,#2c331d 100%)}
.testi-head{top:1356px;font-size:21px;font-weight:500;color:#fff}
.card{left:184px;top:1408px;width:777px;height:297px;background:#fff}
.quote{left:38px;top:34px;font-family:'Playfair Display',serif;font-size:150px;line-height:1;color:var(--red-soft)}
.card h4{position:absolute;left:133px;top:28px;width:600px;font-family:'Playfair Display',serif;font-size:27px;font-weight:500;line-height:37px;color:var(--blue)}
.card p{position:absolute;left:133px;top:116px;width:610px;font-size:14px;line-height:26px;color:#666}
.avatar{left:133px;top:208px;width:56px;height:56px;border-radius:50%;background:linear-gradient(135deg,#9aa,#556)}
.who{position:absolute;left:205px;top:210px}
.who b{display:block;font-size:21px;font-weight:500;color:#555}
.who span{font-size:14px;color:#666}
.dots{top:1737px;display:flex;justify-content:center;gap:5px;padding-right:50px}
.dots i{width:13px;height:13px;border:1.5px solid #fff;border-radius:50%;display:block}
.dots i.on{background:var(--red);border-color:var(--red)}

/* about */
.about-car{left:116px;top:2091px;width:320px;height:169px;border-radius:40% 40% 12% 12%/50% 50% 15% 15%;
  background:linear-gradient(180deg,#b01a22 0%,#d52a30 55%,#3a3a3a 100%)}
.about-text{left:506px;top:2080px;width:585px;font-size:14px;line-height:28px;color:#444}
.about-text p+p{margin-top:28px}
.btn-red{left:506px;top:2290px;width:206px;height:40px;background:var(--red);color:#fff;font-size:16px;font-weight:500;display:flex;align-items:center;justify-content:center;border-radius:2px}

/* footer */
.footer{left:0;top:2430px;width:1200px;height:495px;background:var(--footer);color:#fff}
.col{position:absolute}
.col h5{font-size:22px;font-weight:500;border-left:6px solid var(--red);padding:4px 0 4px 12px;margin-left:-18px}
.col ul{list-style:none;margin-top:8px}
.col li{font-size:14px;line-height:28px}
.news{font-size:16px;line-height:24px;margin-top:10px}
.sub{position:absolute;left:131px;top:392px;width:377px;height:42px;display:flex}
.sub span{flex:1;background:#3a0a09;font-size:14px;display:flex;align-items:center;padding-left:22px}
.sub b{width:121px;background:var(--red);font-size:16px;font-weight:500;display:flex;align-items:center;justify-content:center}
.foot-brand{left:846px;top:62px;width:180px;height:180px;border:2px solid var(--blue);border-radius:50%;display:flex;align-items:center;justify-content:center;font-size:34px;font-weight:500;color:var(--blue)}
.social{left:920px;top:290px;display:flex;gap:20px}
.social i{width:28px;height:28px;border-radius:50%;background:var(--blue);display:block}
.bar{left:0;top:2925px;width:1200px;height:68px;background:var(--bar);color:#fff;font-size:13px}
.bar .copy{position:absolute;left:113px;top:26px}
.bar .links{position:absolute;right:110px;top:26px;word-spacing:2px}
</style>
</head>
<body>

<div class="abs hero" role="img" aria-label="Photo of a traveller in a sun hat beside a silver hatchback on a coastal road"></div>
<div class="abs hero-car" role="img" aria-label="Rear of a silver rental car"></div>

<header class="abs header">
  <div class="abs brand">
    <div class="brand-mark"><span class="brand-name">Marlenic</span><span class="brand-sub">Vehicle Rental</span></div>
  </div>
  <nav class="abs nav">
    <span>Log In <svg width="15" height="15" viewBox="0 0 16 16"><circle cx="8" cy="8" r="8" fill="#444"/><circle cx="8" cy="6" r="2.6" fill="#fff"/><path d="M3.5 13a5 4 0 0 1 9 0" fill="#fff"/></svg></span>
    <span>Help <svg width="15" height="15" viewBox="0 0 16 16"><circle cx="8" cy="8" r="8" fill="#444"/><rect x="7" y="7" width="2" height="5" fill="#fff"/><circle cx="8" cy="4.6" r="1.2" fill="#fff"/></svg></span>
    <span>Menu <svg width="14" height="12" viewBox="0 0 14 12"><rect y="0" width="14" height="2" fill="#444"/><rect y="5" width="14" height="2" fill="#444"/><rect y="10" width="14" height="2" fill="#444"/></svg></span>
    <span class="lang"><i class="flag"></i> English <svg width="10" height="8" viewBox="0 0 10 8"><path d="M1 2l4 4 4-4" stroke="#333" stroke-width="2" fill="none"/></svg></span>
  </nav>
</header>

<h1 class="abs hero-title serif">Looking for a vehicle?</h1>
<div class="abs hero-script">You're at the right place.</div>

<section class="abs booking">
  <h2>Make a Reservation</h2>
  <div class="rule"></div>
  <div class="field" style="left:16px;top:74px;width:302px">Pick up location <svg width="10" height="8"><path d="M1 2l4 4 4-4" stroke="#222" stroke-width="2" fill="none"/></svg></div>
  <div class="field" style="left:336px;top:74px;width:302px">Return location <svg width="10" height="8"><path d="M1 2l4 4 4-4" stroke="#222" stroke-width="2" fill="none"/></svg></div>
  <div class="field" style="left:657px;top:74px;width:302px">Driver's age <svg width="10" height="8"><path d="M1 2l4 4 4-4" stroke="#222" stroke-width="2" fill="none"/></svg></div>
  <div class="chk"><i></i>Pick up location same as return location</div>
  <div class="label" style="left:347px;top:130px">Pick-up Date/Time</div>
  <div class="label" style="left:670px;top:130px">Return Date/Time</div>
  <div class="field" style="left:16px;top:155px;width:302px">Vehicle category <svg width="10" height="8"><path d="M1 2l4 4 4-4" stroke="#222" stroke-width="2" fill="none"/></svg></div>
  <div class="field" style="left:336px;top:155px;width:150px;padding-left:20px">10-04-2024 <svg width="13" height="14"><rect x="0.5" y="2" width="12" height="11.5" fill="none" stroke="#222"/><rect x="0" y="2" width="13" height="3.5" fill="#222"/><path d="M3 6v7M6.5 6v7M10 6v7M0 9.5h13" stroke="#222"/></svg></div>
  <div class="field" style="left:488px;top:155px;width:150px;padding-left:42px">09:00 <svg width="15" height="15"><circle cx="7.5" cy="7.5" r="7.5" fill="#111"/><path d="M7.5 3.5v4.5l3 2" stroke="#fff" stroke-width="1.6" fill="none"/></svg></div>
  <div class="field" style="left:657px;top:155px;width:150px;padding-left:20px">10-04-2024 <svg width="13" height="14"><rect x="0.5" y="2" width="12" height="11.5" fill="none" stroke="#222"/><rect x="0" y="2" width="13" height="3.5" fill="#222"/><path d="M3 6v7M6.5 6v7M10 6v7M0 9.5h13" stroke="#222"/></svg></div>
  <div class="field" style="left:809px;top:155px;width:150px;padding-left:42px">09:00 <svg width="15" height="15"><circle cx="7.5" cy="7.5" r="7.5" fill="#111"/><path d="M7.5 3.5v4.5l3 2" stroke="#fff" stroke-width="1.6" fill="none"/></svg></div>
  <div class="search">Search</div>
</section>

<section>
  <h2 class="abs center sec-title" style="top:774px">Why Choose Marlenic Limited?</h2>
  <div class="abs center" style="top:827px"><div class="divider"></div></div>
  <p class="abs center lead" style="top:842px">Lorem ipsum is placeholder text commonly used in the graphic, print, and publishing industries<br>for previewing layouts and visual mockups.</p>

  <div class="abs feature" style="left:96px;top:954px">
    <div class="ring"><svg width="76" height="70" viewBox="0 0 76 70" fill="none" stroke="#c7302b" stroke-width="2.5"><circle cx="38" cy="16" r="13"/><path d="M40 8l-6 9h7l-5 8"/><path d="M16 48l6-12h32l6 12v12H16z"/><path d="M4 44l4-8h10M72 44l-4-8H58"/><circle cx="26" cy="52" r="3"/><circle cx="50" cy="52" r="3"/></svg></div>
    <h3>Accessible</h3>
    <p>Lorem ipsum is placeholder text common-<br>ly used in the graphic, print,</p>
  </div>
  <div class="abs feature" style="left:452px;top:954px">
    <div class="ring"><svg width="76" height="70" viewBox="0 0 76 70" fill="none" stroke="#c7302b" stroke-width="2.5"><path d="M8 38l7-16h34l7 16v14H8z"/><path d="M8 30H2M62 30h-6"/><circle cx="18" cy="42" r="3"/><path d="M48 34l16-5 10 5v14c0 8-10 14-10 14s-16-6-16-14z" fill="#fff"/><path d="M56 46l5 5 8-9"/></svg></div>
    <h3>Secure</h3>
    <p>Lorem ipsum is placeholder text common-<br>ly used in the graphic, print,</p>
  </div>
  <div class="abs feature" style="left:806px;top:954px">
    <div class="ring"><svg width="76" height="70" viewBox="0 0 76 70" fill="none" stroke="#c7302b" stroke-width="2.5"><rect x="6" y="10" width="52" height="46" rx="3"/><path d="M6 22h52M16 5v10M28 5v10M40 5v10M52 5v10M14 32h14M14 40h20M14 48h14"/><circle cx="56" cy="50" r="14" fill="#fff" stroke-dasharray="4 3"/><path d="M56 42v8l5 4"/></svg></div>
    <h3>Convenient</h3>
    <p>Lorem ipsum is placeholder text common-<br>ly used in the graphic, print,</p>
  </div>
</section>

<section>
  <div class="abs testi-bg" role="img" aria-label="Photo of a woman leaning out of a car window in green hills under a blue sky"></div>
  <h2 class="abs center serif testi-head">Our Happy Customers Says</h2>
  <article class="abs card">
    <div class="abs quote">&ldquo;</div>
    <h4>Marlenic Limited Lorem ipsum dolor sit amet, consectetur adipiscing.</h4>
    <p>Lorem ipsum dolor sit amet, consectetur adipiscing elit, sed do eiusmod tempor incididunt ut labore et dolore magna aliqua. Ut enim ad minim veniam, quis nostrud exercitation ullamco laboris nisi ut aliquip ex ea commodo consequat.</p>
    <div class="abs avatar" role="img" aria-label="Customer portrait"></div>
    <div class="who"><b>Clara M. Duarte</b><span>Credit checker</span></div>
  </article>
  <div class="abs center dots"><i class="on"></i><i></i><i></i><i></i></div>
</section>

<section>
  <h2 class="abs center sec-title" style="top:1931px">About Us Marlenic Limited</h2>
  <div class="abs center" style="top:1985px"><div class="divider"></div></div>
  <p class="abs center lead" style="top:2000px">Lorem ipsum is placeholder text commonly used in the graphic, print, and publishing industries<br>for previewing layouts and visual mockups.</p>
  <div class="abs about-car" role="img" aria-label="Photo of a red saloon car"></div>
  <div class="abs about-text">
    <p>Lorem ipsum dolor sit amet, consectetur adipiscing elit, sed do eiusmod tempor incididunt ut labore et dolore magna aliqua. Ut enim ad minim veniam, quis nostrud exercitation ullamco laboris nisi ut aliquip ex ea commodo consequat.</p>
    <p>Duis aute irure dolor in reprehenderit in voluptate velit esse cillum dolore eu fugiat nulla pariatur. Excepteur sint occaecat cupidatat non proident, sunt in culpa qui officia deserunt mollit anim id est laborum.</p>
  </div>
  <div class="abs btn-red">Read More About Us</div>
</section>

<footer class="abs footer">
  <div class="col" style="left:130px;top:60px">
    <h5>Legal Information</h5>
    <ul><li>Damage Management Policy</li><li>Deposit Policy</li><li>Security and privacy policy</li><li>Terms and conditions</li><li>Important information</li></ul>
  </div>
  <div class="col" style="left:130px;top:268px">
    <h5>Exclusive offers</h5>
    <p class="news">Sign up to our newsletter to receive<br>our latest offers</p>
  </div>
  <div class="sub"><span>Email Address</span><b>Subscriber</b></div>
  <div class="col" style="left:586px;top:64px">
    <h5>More information</h5>
    <ul><li>Terms and Conditions</li><li>Privacy Policy</li><li>FAQ &amp; Help</li><li>Legal Notice</li><li>Fleet</li><li>Informations - Algarve</li><li>Extras &amp; Services</li><li>Partners</li><li>Contacts</li><li>Sitemap</li></ul>
  </div>
  <div class="abs foot-brand">Marlenic</div>
  <div class="abs social" aria-label="Social links"><i></i><i></i><i></i><i></i></div>
</footer>
<div class="abs bar">
  <span class="copy">Marlenic Limited. © 2024 All Rights Reserved</span>
  <span class="links">Site map &nbsp;|&nbsp; Legal mentions &nbsp;|&nbsp; Cookies, Security and Privacy policy &nbsp;|&nbsp; Contact us</span>
</div>

</body>
</html>
```